Award-winnning Estate Agent needs a premium version of their 'For Sale' board design

We need a premium option for our 'For Sale' board design. We have a standard board that is attached to this brief, but were are looking to have a premium design version that we will use when selling exclusive properties. Our company name is Harbourline Row Estates and the name for this is exclusive selection is: 'The Harbourline Portfolio'. The design needs to work with our current brand, but have a distinctive PREMIUM feel to it. I have uploaded the barnd guidelines and also some of the exisisting logo variations. We do NOT need a new logo but feel free to play around with colours, fonts, sizes etc. for the sign.

Target Market(s)

Property buyers & house hunters

Industry/Entity Type

Real Estate - Residential Property

Font styles to use
Sans Serif

Requirements
Must have
• A premium fee, must be square design, must be easy to read when driving past the sign
Nice to have
• I'm open ot ideas

```html
<!DOCTYPE html>
<html lang="en">
<head>
<meta charset="utf-8">
<title>The Harbourline Portfolio – For Sale Board</title>
<link rel="stylesheet" href="https://fonts.googleapis.com/css2?family=Archivo+Black&family=Arimo:wght@400;700&display=swap">
<style>
  :root {
    --navy: #021436;
    --gold: #b39a53;
    --white: #ffffff;
    --backdrop: #e8e8e6;
  }
  * { margin: 0; padding: 0; box-sizing: border-box; }
  html, body {
    width: 720px;
    height: 1200px;
    overflow: hidden;
    background: var(--backdrop);
  }
  .sale-board {
    position: absolute;
    left: 0;
    top: 240px;
    width: 720px;
    height: 720px;
    background: var(--navy);
    font-family: "Arimo", Arial, sans-serif;
  }
  .board-frame {
    position: absolute;
    left: 20px;
    top: 19px;
    right: 20px;
    bottom: 22px;
    border: 3px solid var(--gold);
  }
  .headline-band {
    position: absolute;
    left: 0;
    right: 0;
    top: 48px;
    height: 161px;
    background: var(--gold);
    display: flex;
    align-items: center;
    justify-content: center;
  }
  .headline {
    font-family: "Archivo Black", "Arial Black", sans-serif;
    font-size: 116px;
    line-height: 1;
    color: var(--white);
    letter-spacing: 1px;
    padding-top: 6px;
  }
  .brand-mark {
    position: absolute;
    left: 312px;
    top: 290px;
    width: 96px;
    height: 96px;
    background: var(--white);
  }
  .brand-name {
    position: absolute;
    left: 0;
    right: 0;
    top: 432px;
    text-align: center;
    font-size: 48px;
    font-weight: 400;
    color: var(--white);
    letter-spacing: -0.5px;
    line-height: 1;
  }
  .divider {
    position: absolute;
    left: 243px;
    top: 518px;
    width: 235px;
    height: 4px;
    background: var(--gold);
  }
  .phone {
    position: absolute;
    left: 0;
    right: 0;
    top: 538px;
    text-align: center;
    font-family: "Archivo Black", "Arial Black", sans-serif;
    font-size: 62px;
    line-height: 1;
    color: var(--white);
    letter-spacing: 2px;
    word-spacing: 10px;
  }
  .website {
    position: absolute;
    left: 0;
    right: 0;
    top: 618px;
    text-align: center;
    font-size: 37px;
    line-height: 1;
    color: var(--gold);
  }
</style>
</head>
<body>
  <section class="sale-board" aria-label="For Sale board">
    <div class="board-frame"></div>
    <div class="headline-band">
      <h1 class="headline">FOR SALE</h1>
    </div>
    <div class="brand-mark" aria-hidden="true"></div>
    <p class="brand-name">The Harbourline Portfolio</p>
    <div class="divider"></div>
    <p class="phone">01632 960418</p>
    <p class="website">www.harbourlinerowestates.co.uk</p>
  </section>
</body>
</html>
```